Larkspur Stillness

Logo picture and I want it to say

yoga. meditation. sound healing

small sweet classes

Larkspur-stillness.com

2740 West Hollander Ave Suite K
Santa Barbara ca 93108

```html
<!DOCTYPE html>
<html lang="en">
<head>
<meta charset="utf-8">
<title>Larkspur Stillness – Flyer</title>
<link rel="stylesheet" href="https://fonts.googleapis.com/css2?family=Questrial&family=Open+Sans:wght@400;700&display=swap">
<style>
  :root {
    --page-bg: #ececec;
    --navy: #3a3d6d;
    --plum-blob: #7b6c96;
    --pink-top: #bb8cc0;
    --lavender-mid: #9c80c6;
    --blue-violet: #6d62b6;
    --photo-light: #e9e6e3;
    --photo-dark: #4a4745;
    --white: #ffffff;
  }
  * { margin: 0; padding: 0; box-sizing: border-box; }
  html, body {
    width: 1084px;
    height: 1200px;
    overflow: hidden;
    background: var(--page-bg);
  }
  .flyer {
    position: absolute;
    left: 79px;
    top: 0;
    width: 926px;
    height: 1200px;
    overflow: hidden;
    font-family: "Open Sans", Arial, sans-serif;
    color: var(--white);
  }
  .flyer-shapes {
    position: absolute;
    inset: 0;
    width: 100%;
    height: 100%;
  }
  .brand-badge {
    position: absolute;
    left: 641px;
    top: 435px;
    width: 236px;
    height: 236px;
    border: 3px solid var(--white);
    border-radius: 50%;
    display: flex;
    align-items: center;
    justify-content: center;
    text-align: center;
  }
  .brand-name {
    font-family: "Open Sans", Arial, sans-serif;
    font-weight: 400;
    font-size: 28px;
    line-height: 1.2;
    color: var(--white);
  }
  .headline {
    position: absolute;
    left: 0;
    right: 0;
    top: 852px;
    text-align: center;
    font-family: "Questrial", Arial, sans-serif;
    font-size: 51px;
    font-weight: 400;
    letter-spacing: 0.2px;
  }
  .subhead {
    position: absolute;
    left: 0;
    right: 0;
    top: 938px;
    text-align: center;
    font-size: 30px;
    font-weight: 700;
    letter-spacing: 0.3px;
  }
  .web-pill {
    position: absolute;
    left: 138px;
    top: 1004px;
    width: 656px;
    height: 44px;
    border-radius: 22px;
    background: var(--navy);
    display: flex;
    align-items: center;
    justify-content: center;
    gap: 10px;
    font-size: 25px;
    font-weight: 700;
  }
  .web-icon { width: 22px; height: 22px; }
  .address {
    position: absolute;
    left: 0;
    right: 0;
    top: 1077px;
    text-align: center;
    font-size: 21px;
    font-weight: 400;
  }
</style>
</head>
<body>
  <main class="flyer">
    <svg class="flyer-shapes" viewBox="0 0 611 792" preserveAspectRatio="none" aria-hidden="false">
      <defs>
        <linearGradient id="photoTone" x1="0" y1="0" x2="0" y2="1">
          <stop offset="0" stop-color="var(--photo-light)"/>
          <stop offset="0.45" stop-color="#c9c4bf"/>
          <stop offset="1" stop-color="var(--photo-dark)"/>
        </linearGradient>
        <linearGradient id="lowerTone" x1="0.2" y1="0" x2="0.5" y2="1">
          <stop offset="0" stop-color="var(--pink-top)"/>
          <stop offset="0.5" stop-color="var(--lavender-mid)"/>
          <stop offset="1" stop-color="var(--blue-violet)"/>
        </linearGradient>
      </defs>
      <rect class="class-photo" x="0" y="0" width="611" height="420" fill="url(#photoTone)"
            role="img" aria-label="Photo of a yoga class holding side plank poses on mats in a bright studio"/>
      <path class="corner-blob" d="M0,0 L120,0 C95,10 72,40 62,80 C52,115 28,132 0,136 Z" fill="var(--plum-blob)"/>
      <path class="navy-wave" d="M0,375 C120,420 250,420 360,330 C450,258 540,212 611,195 L611,520 L0,520 Z" fill="var(--navy)"/>
      <path class="lower-panel" d="M0,500 Q300,395 611,495 L611,792 L0,792 Z" fill="url(#lowerTone)"/>
    </svg>

    <div class="brand-badge">
      <span class="brand-name">Larkspur<br>Stillness</span>
    </div>

    <h1 class="headline">Yoga. Meditation. Sound Healing</h1>
    <p class="subhead">SMALL SWEET CLASSES</p>

    <div class="web-pill">
      <svg class="web-icon" viewBox="0 0 24 24" fill="none" stroke="#ffffff" stroke-width="1.6" aria-hidden="true">
        <circle cx="12" cy="12" r="10"/>
        <ellipse cx="12" cy="12" rx="4.5" ry="10"/>
        <line x1="2" y1="12" x2="22" y2="12"/>
        <path d="M4,7 H20 M4,17 H20"/>
      </svg>
      <span>Larkspur-stillness.com</span>
    </div>

    <p class="address">2740 West Hollander Ave Suite K Santa Barbara Ca 93108</p>
  </main>
</body>
</html>
```